K&T Fixit and Rebuild general contracting business card design

I already have a logo that I want to use and I need a card that uses that logo and color scheme on the front with the address phone numbers and email and on the back a place for technicians to write in their name and phone number when they hand it out. It will need the License number of License #KTFXTRB318QN.
It should say General Contractor under the company name. The address is
4417 NE 3rd St, Ste D226
Vancouver, WA 98652
www.kandtfixitandrebuild.example
office@kandtfixitandrebuild.example
360-555-0142 is the telephone number
360-555-0187 is the fax number

Target Market(s)

Homeowners needing remodel work or repairs in their home.

Industry/Entity Type

Construction

Contact Information for Business Card

Business name, address, phone number, license number, fax number, email, and website on the front and a place to fill in technician's name and number

Font styles to use
Serif

Requirements
Must have
• Business name, address, phone number, license number, fax number, email, and website on the front and a place to fill in technician's name and number
Nice to have
• I uploaded an example of a front that is good.
Should not have
• Froo froo or extra embellishments.

```html
<!DOCTYPE html>
<html lang="en">
<head>
<meta charset="utf-8">
<title>K&amp;T Fixit and Rebuild – Business Card</title>
<link href="https://fonts.googleapis.com/css2?family=Open+Sans:wght@400;700&family=Michroma&display=swap" rel="stylesheet">
<style>
  :root {
    --page: #e4e4e4;
    --card-white: #f4f4f4;
    --wood-dark: #5a2a10;
    --wood-mid: #8a4520;
    --wood-light: #a65e30;
    --brown: #8b4a22;
    --brown-deep: #3d1f0e;
    --ink: #3a2418;
    --white: #ffffff;
  }
  * { margin: 0; padding: 0; box-sizing: border-box; }
  html, body { width: 1200px; height: 960px; overflow: hidden; }
  body {
    background: var(--page);
    font-family: "Open Sans", Arial, sans-serif;
    position: relative;
  }
  .card {
    position: absolute;
    left: 310px;
    width: 590px;
    height: 338px;
    border-radius: 18px;
    overflow: hidden;
  }
  /* Technician side */
  .card-tech { top: 127px; }
  .wood-backdrop {
    position: absolute; inset: 0;
    background: linear-gradient(135deg, var(--wood-dark) 0%, var(--wood-mid) 45%, var(--wood-light) 60%, var(--wood-mid) 80%, var(--wood-dark) 100%);
  }
  .tech-brand {
    position: absolute; left: 0; right: 0; top: 104px;
    text-align: center;
    color: var(--white);
    font-weight: 700;
    font-size: 40px;
    letter-spacing: 0.5px;
  }
  .tech-tagline {
    position: absolute; left: 0; right: 0; top: 227px;
    text-align: center;
    color: var(--white);
    font-family: "Michroma", Arial, sans-serif;
    font-size: 15px;
    letter-spacing: 1px;
    text-transform: uppercase;
  }
  .write-in {
    position: absolute; left: 30px; top: 278px;
    width: 528px; height: 36px;
    background: var(--card-white);
    border-radius: 18px;
    color: var(--ink);
    font-size: 16px;
    line-height: 36px;
  }
  .write-in .field-name { position: absolute; left: 13px; }
  .write-in .field-contact { position: absolute; left: 311px; }

  /* Contact side */
  .card-info { top: 517px; background: var(--card-white); }
  .info-brand {
    position: absolute; left: 0; right: 0; top: 110px;
    text-align: center;
    color: var(--brown);
    font-weight: 700;
    font-size: 36px;
  }
  .license {
    position: absolute; left: 0; right: 0; top: 197px;
    text-align: center; color: var(--ink); font-size: 16px;
  }
  .contact-list {
    position: absolute; left: 0; right: 0; top: 232px;
    list-style: none; text-align: center;
    color: var(--ink); font-size: 16px; line-height: 20px;
  }
  .contact-list li span + span { margin-left: 10px; }
  .icon { display: inline-block; width: 13px; height: 13px; vertical-align: -1px; margin-right: 3px; }
  .address-band { position: absolute; left: 0; bottom: 0; width: 590px; height: 34px; }
  .address {
    position: absolute; left: 0; right: 0; bottom: 7px;
    text-align: center; color: var(--white); font-size: 16px;
  }
</style>
</head>
<body>
  <section class="card card-tech" aria-label="Technician side">
    <div class="wood-backdrop" role="img" aria-label="Photo of wooden planks with a hammer, wrenches, pliers, tape measure, level and nails around the edges"></div>
    <div class="tech-brand">K&amp;T Fixit and Rebuild</div>
    <div class="tech-tagline">General Contractor</div>
    <div class="write-in">
      <span class="field-name">Name</span>
      <span class="field-contact">Contact</span>
    </div>
  </section>

  <section class="card card-info" aria-label="Contact side">
    <div class="info-brand">K&amp;T Fixit and Rebuild</div>
    <p class="license">License #KTFXTRB318QN</p>
    <ul class="contact-list">
      <li>
        <span><svg class="icon" viewBox="0 0 16 16"><path fill="#8b4a22" d="M3 1l3 3-1.5 2a9 9 0 0 0 5.5 5.5L12 10l3 3-2 2C7 15 1 9 1 3z"/></svg>360-555-0142</span>
        <span><svg class="icon" viewBox="0 0 16 16"><rect x="4" y="1" width="8" height="5" fill="#8b4a22"/><rect x="1" y="6" width="14" height="7" rx="1" fill="#8b4a22"/><rect x="4" y="10" width="8" height="5" fill="#f4f4f4" stroke="#8b4a22"/></svg>360-555-0187</span>
      </li>
      <li><svg class="icon" viewBox="0 0 16 16"><rect x="1" y="3" width="14" height="10" fill="none" stroke="#8b4a22" stroke-width="1.6"/><path d="M1 3l7 6 7-6" fill="none" stroke="#8b4a22" stroke-width="1.6"/></svg>office@kandtfixitandrebuild.example</li>
      <li><svg class="icon" viewBox="0 0 16 16"><circle cx="8" cy="8" r="6.5" fill="none" stroke="#8b4a22" stroke-width="1.4"/><path d="M1.5 8h13M8 1.5c-3 3.5-3 9.5 0 13M8 1.5c3 3.5 3 9.5 0 13" fill="none" stroke="#8b4a22" stroke-width="1.2"/></svg>www.kandtfixitandrebuild.example</li>
    </ul>
    <svg class="address-band" viewBox="0 0 590 34" aria-hidden="true">
      <rect x="0" y="14" width="590" height="20" fill="var(--brown-deep)"/>
      <polygon points="66,34 84,0 506,0 524,34" fill="var(--card-white)"/>
      <polygon points="72,34 88,3 502,3 518,34" fill="var(--brown)"/>
    </svg>
    <p class="address">4417 NE 3rd St, Ste D226, Vancouver, WA 98652</p>
  </section>
</body>
</html>
```